Carton Box Packaging For Motorcycle Brake Shoe - Varonel Brand

Packaging Dimensions: 125mm (H) x 125mm (W) x 31mm (D)
We would like to design a genuine Carton box Packaging for motorcycle Brake Shoe.
This is a critical part of the motorcycle, so we need the packaging to reflect elegant impression.
Varonel, is one of the leading companies for manufacturing Motorcycles, located in Egypt. Our company is offering high-quality products, the best in the local market, with very competitive prices.
We have a limited time to get this project done, So we Highly appreciate receiving your designs ASAP.
Target Market(s)
Economical Motorcycle Buyers
Colors
Designer to choose colors to be used in the design.
Look and feel

```html
<!DOCTYPE html>
<html lang="en">
<head>
<meta charset="utf-8">
<title>Varonel Motorcycle Brake Shoe – Carton Box</title>
<link rel="stylesheet" href="https://fonts.googleapis.com/css2?family=Baloo+2:wght@800&display=swap">
<style>
  :root {
    --bg: #ffffff;
    --box-blue: #1f4a9c;
    --brand-red: #d71f2b;
    --pale-grey: #e9eef0;
    --white: #ffffff;
  }
  html, body {
    margin: 0;
    width: 1200px;
    height: 1200px;
    overflow: hidden;
    background: var(--bg);
  }
  .canvas {
    position: relative;
    width: 1200px;
    height: 1200px;
  }
  .lid {
    position: absolute;
    left: 150px;
    top: 150px;
    width: 700px;
    height: 700px;
    overflow: hidden;
  }
  .lid svg { display: block; }
  .front-panel,
  .right-panel {
    position: absolute;
    background: var(--box-blue);
    overflow: hidden;
  }
  .front-panel {
    left: 150px;
    top: 850px;
    width: 700px;
    height: 175px;
    display: flex;
    align-items: center;
    padding-left: 110px;
    box-sizing: border-box;
  }
  .right-panel {
    left: 850px;
    top: 150px;
    width: 175px;
    height: 700px;
  }
  .right-panel .rotated {
    position: absolute;
    left: 50%;
    top: 50%;
    width: 700px;
    height: 175px;
    transform: translate(-50%, -50%) rotate(90deg);
    display: flex;
    align-items: center;
    justify-content: center;
  }
  .product-title {
    margin: 0;
    font-family: "Baloo 2", sans-serif;
    font-weight: 800;
    color: var(--brand-red);
    -webkit-text-stroke: 3px var(--white);
    paint-order: stroke fill;
    line-height: 0.82;
    letter-spacing: -1px;
  }
  .product-title span { display: block; }
  .lid .product-title {
    position: absolute;
    right: 30px;
    top: 190px;
    text-align: right;
  }
  .lid .line-small { font-size: 56px; }
  .lid .line-large { font-size: 78px; }
  .front-panel .line-small,
  .right-panel .line-small { font-size: 52px; }
  .front-panel .line-large,
  .right-panel .line-large { font-size: 72px; }
  .brand-mark {
    position: absolute;
    left: 330px;
    top: 530px;
    display: flex;
    align-items: center;
    gap: 12px;
  }
  .brand-mark .dot {
    width: 48px;
    height: 48px;
    border-radius: 50%;
    background: var(--white);
  }
  .brand-mark .name {
    font-family: "Baloo 2", sans-serif;
    font-weight: 800;
    font-size: 50px;
    color: var(--white);
  }
</style>
</head>
<body>
<div class="canvas">
  <section class="lid">
    <svg width="700" height="700" viewBox="0 0 700 700">
      <defs>
        <linearGradient id="stripe-tone" x1="0" y1="0" x2="1" y2="1">
          <stop offset="0" stop-color="#7a3570"/>
          <stop offset="0.6" stop-color="#4a3d8c"/>
          <stop offset="1" stop-color="#2e4294"/>
        </linearGradient>
      </defs>
      <rect class="lid-base" width="700" height="700" fill="var(--box-blue)"/>
      <rect class="stripe-field" x="250" y="0" width="450" height="700" fill="url(#stripe-tone)" role="img" aria-label="Fine red and blue horizontal line pattern"/>
      <path class="red-sweep" d="M0 0 H300 C260 60 250 110 250 170 C170 110 90 95 0 110 Z" fill="var(--brand-red)"/>
      <circle class="blue-ring" cx="130" cy="330" r="270" fill="var(--box-blue)"/>
      <circle class="grey-disc" cx="110" cy="330" r="235" fill="var(--pale-grey)"/>
      <rect class="shoe-drawing" x="20" y="200" width="250" height="250" rx="125" fill="#c9d6e6" role="img" aria-label="Line drawing of a pair of brake shoes with springs"/>
      <rect class="rider-art" x="310" y="15" width="200" height="160" fill="#c98fa6" opacity="0.6" role="img" aria-label="Illustration of a motorcycle rider"/>
    </svg>
    <h1 class="product-title"><span class="line-small">motorcycle</span><span class="line-large">brake shoe</span></h1>
    <div class="brand-mark"><span class="dot"></span><span class="name">Varonel</span></div>
  </section>
  <section class="front-panel">
    <h2 class="product-title"><span class="line-small">motorcycle</span><span class="line-large">brake shoe</span></h2>
  </section>
  <section class="right-panel">
    <div class="rotated">
      <h2 class="product-title"><span class="line-small">motorcycle</span><span class="line-large">brake shoe</span></h2>
    </div>
  </section>
</div>
</body>
</html>
```